Young Entrepreneur needs the sexiest, slickest, hottest ANDROID ALARM APP DESIGN.

Now that I have your attention...

The name of the Application is PlumDrift, using 'Stickers' this application is meant to get you to do what you need to do AND TO DO IT NOW, with a UI so simple my grandma can use it.

Using the provided sketches as a REFERENCE point, THREE (3) SCREENS will be needed, including a couple of design accents, which when the project is completed will be sent directly to a programming team.

Industry/Entity Type

Android

Requirements
Must have
• Creativity in simplicity. but please, go wild, do your 'thang'... Just keep it simple and clean.

```html
<!DOCTYPE html>
<html lang="en">
<head>
<meta charset="utf-8">
<title>PlumDrift – Set Sticky</title>
<link rel="stylesheet" href="https://fonts.googleapis.com/css2?family=Exo+2:wght@400;500;600;700&display=swap">
<style>
  :root {
    --bg: #3f5e6b;
    --string: #6b838d;
    --drop: #6b838d;
    --drop-label: #263b45;
    --bubble: #cdd6db;
    --time: #7f8b91;
    --title: #263b45;
    --day: #8b989e;
    --save: #4a6370;
    --caption: #d6dee2;
  }
  html, body {
    margin: 0;
    padding: 0;
    width: 720px;
    height: 1200px;
    overflow: hidden;
    background: var(--bg);
  }
  .screen {
    position: relative;
    width: 720px;
    height: 1200px;
    overflow: hidden;
    background: var(--bg);
    font-family: "Exo 2", sans-serif;
  }
  .scene { position: absolute; inset: 0; }
  .string { stroke: var(--string); stroke-width: 2; }
  .drop { fill: var(--drop); }
  .drop-label {
    fill: var(--drop-label);
    font-size: 23px;
    font-weight: 600;
    text-anchor: middle;
  }
  .task-bubble { fill: var(--bubble); }
  .task-time { fill: var(--time); font-size: 34px; font-weight: 700; }
  .task-time-suffix { font-size: 16px; font-weight: 600; }
  .task-title { fill: var(--title); font-size: 46px; font-weight: 500; text-anchor: middle; letter-spacing: 1px; }
  .task-day { fill: var(--day); font-size: 25px; font-weight: 400; text-anchor: middle; }
  .task-save { fill: var(--save); font-size: 31px; font-weight: 500; text-anchor: middle; letter-spacing: 1px; }
  .toggle-ring { fill: var(--string); }
  .toggle-face { fill: var(--bubble); }
  .toggle-label { fill: var(--title); font-size: 18px; font-weight: 700; text-anchor: middle; }
  .tool-ring { fill: var(--string); }
  .tool-face { fill: var(--bubble); }
  .tool-glyph { fill: var(--title); }
  .tool-stroke { fill: none; stroke: var(--title); stroke-width: 2.2; stroke-linecap: round; }
  .tool-label { fill: var(--title); font-size: 20px; font-weight: 700; text-anchor: middle; }
  .colour-picker {
    position: absolute;
    left: 338px;
    top: 408px;
    width: 48px;
    height: 48px;
    border-radius: 50%;
    background: conic-gradient(from 0deg,
      #f5e83a 0 30deg, #f9b62a 30deg 60deg, #f47a25 60deg 90deg, #ee3b2a 90deg 120deg,
      #e52956 120deg 150deg, #c4268c 150deg 180deg, #8a2fb0 180deg 210deg, #4a34c4 210deg 240deg,
      #2b4fe0 240deg 270deg, #1e9be0 270deg 300deg, #22c25a 300deg 330deg, #9ad836 330deg 360deg);
  }
  .caption {
    fill: var(--caption);
    font-size: 40px;
    font-weight: 400;
    text-anchor: middle;
    letter-spacing: 1px;
  }
  .brand-base { fill: var(--drop); }
  .brand-name {
    fill: var(--bg);
    font-size: 37px;
    font-weight: 600;
    text-anchor: middle;
  }
</style>
</head>
<body>
<main class="screen">
  <svg class="scene" width="720" height="1200" viewBox="0 0 720 1200" xmlns="http://www.w3.org/2000/svg">
    <defs>
      <path id="drop-shape" d="M0,0 C15,40 49,70 49,106 A49,49 0 0 1 -49,106 C-49,70 -15,40 0,0 Z"/>
    </defs>

    <g class="strings">
      <line class="string" x1="118" y1="0" x2="118" y2="224"/>
      <line class="string" x1="200" y1="0" x2="200" y2="384"/>
      <line class="string" x1="281" y1="0" x2="281" y2="538"/>
      <line class="string" x1="362" y1="0" x2="362" y2="697"/>
      <line class="string" x1="443" y1="0" x2="443" y2="540"/>
      <line class="string" x1="524" y1="0" x2="524" y2="384"/>
      <line class="string" x1="606" y1="0" x2="606" y2="224"/>
    </g>

    <g class="weekday-drops">
      <g transform="translate(117 223)"><use class="drop" href="#drop-shape"/><text class="drop-label" y="107">SUN</text></g>
      <g transform="translate(198 383)"><use class="drop" href="#drop-shape"/><text class="drop-label" y="106">MON</text></g>
      <g transform="translate(280 537)"><use class="drop" href="#drop-shape"/><text class="drop-label" y="106">TUE</text></g>
      <g transform="translate(361 696)"><use class="drop" href="#drop-shape"/><text class="drop-label" y="105">WED</text></g>
      <g transform="translate(442 539)"><use class="drop" href="#drop-shape"/><text class="drop-label" y="107">THU</text></g>
      <g transform="translate(523 383)"><use class="drop" href="#drop-shape"/><text class="drop-label" y="106">FRI</text></g>
      <g transform="translate(604 223)"><use class="drop" href="#drop-shape"/><text class="drop-label" y="107">SAT</text></g>
    </g>

    <g class="task-card">
      <circle class="task-bubble" cx="364" cy="188" r="122"/>
      <text class="task-time" x="314" y="162">6:50<tspan class="task-time-suffix">am</tspan></text>
      <text class="task-title" x="361" y="206">Shower</text>
      <text class="task-day" x="361" y="238">Tuesday</text>
      <text class="task-save" x="364" y="286">Save</text>
      <g class="alarm-toggle">
        <circle class="toggle-ring" cx="441" cy="86" r="30"/>
        <circle class="toggle-face" cx="441" cy="86" r="25"/>
        <text class="toggle-label" x="441" y="93">OFF</text>
      </g>
    </g>

    <g class="tool sound-tool">
      <circle class="tool-ring" cx="362" cy="363" r="24"/>
      <circle class="tool-face" cx="362" cy="363" r="19"/>
      <path class="tool-glyph" d="M351,359 h5 l7,-7 v22 l-7,-7 h-5 z"/>
      <path class="tool-stroke" d="M366,358 a6,6 0 0 1 0,10"/>
      <path class="tool-stroke" d="M369,354 a11,11 0 0 1 0,18"/>
    </g>

    <g class="tool colour-tool">
      <circle class="tool-ring" cx="362" cy="432" r="30"/>
    </g>

    <g class="tool delete-tool">
      <circle class="tool-ring" cx="360" cy="502" r="24"/>
      <circle class="tool-face" cx="360" cy="502" r="19"/>
      <text class="tool-label" x="360" y="509">X</text>
    </g>

    <text class="caption" x="358" y="980">Set Sticky</text>

    <g class="brand">
      <circle class="brand-base" cx="360" cy="1200" r="131"/>
      <text class="brand-name" x="358" y="1164">PlumDrift</text>
    </g>
  </svg>
  <div class="colour-picker" aria-label="Colour picker"></div>
</main>
</body>
</html>
```